International IT and cyber security consulting company is looking to establish a web presence.

Halvern Ridge Advisory LLC provides IT, cyber security, risk, project management and data analytics consulting services worldwide. Our clients are both government and corporate. We are looking to establish a basic web presence with about 6 pages (Home, About Halvern, Our Experts, News and Events, Careers, Contact Us). The designs should set the look and feel of the site for further build out down the line. The final design should be straightforward and simple and allow us to convey information about our consulting services clearly.

Target Market(s)

Government and corporate clients or potential clients, job seekers.

Industry/Entity Type

Consulting

Contact Information for Business Card

The cards will have english on the front and arabic on the back. The design should be the same on both sides.

Coding

Number of Pages Required

Font styles to use
Serif
Sans Serif

Requirements
Must have
• The pages should be simple but visually appealing with a picture or graphic that is appropriate to the company or services we offer. Our name and logo should be branded throughout the design. While we are mostly an IT company we also have a line of business where we organize speaking events for VIPs so the website shouldn't overly emphasize our IT work.
Should not have
• No cartoons or drawings. The site should not have overly flashy or loud colors. We cater to a conservative set of clients so the site should match what they expect to see in an international consultancy's website. There should not be an overuse of the color orange because it can be hard on the eyes if it is used too much on the page. Also, please do not use graphics or pictures that use locks, keys, castles, shields etc since these are too commonly used in the cyber security industry.

```html
<!DOCTYPE html>
<html lang="en">
<head>
<meta charset="utf-8">
<title>Halvern Ridge Advisory LLC</title>
<link href="https://fonts.googleapis.com/css2?family=Titillium+Web:wght@400;600;700&family=Lato:wght@400;700&display=swap" rel="stylesheet">
<style>
:root{
  --orange:#f26a1b;
  --orange-2:#f58634;
  --ink:#1e1e1e;
  --text:#4a4a4a;
  --muted:#7a7a7a;
  --dark:#2f2f31;
  --dark-2:#1b1b1c;
  --peach:#fdf1e8;
  --line:#cfcfcf;
  --white:#ffffff;
}
*{box-sizing:border-box;margin:0;padding:0}
html,body{width:1200px;height:4570px;overflow:hidden}
body{position:relative;font-family:"Lato",sans-serif;color:var(--text);background:var(--white)}
.abs{position:absolute}
.center{left:0;width:1200px;text-align:center}
.heading-font{font-family:"Titillium Web",sans-serif}
.eyebrow{font-family:"Titillium Web",sans-serif;font-size:19px;letter-spacing:1px;color:#333;text-transform:uppercase}
.section-title{font-family:"Titillium Web",sans-serif;font-weight:700;font-size:38px;letter-spacing:4px;color:var(--ink);text-transform:uppercase}
.copy{font-size:14.5px;line-height:26px;color:#555}
.btn{display:inline-block;border-radius:22px;font-family:"Titillium Web",sans-serif;font-weight:600;font-size:14px;text-transform:uppercase;text-align:center;line-height:42px;height:42px}
.btn-fill{background:linear-gradient(90deg,#f0561a,var(--orange-2));color:#fff}
.btn-line{border:1.5px solid var(--orange);color:#fff;line-height:39px}
.vline{position:absolute;left:600px;width:1px;background:var(--line)}

/* hero */
.hero{top:0;left:0;width:1200px;height:625px}
.hero-backdrop{position:absolute;left:0;top:0;width:1200px;height:625px;background:radial-gradient(ellipse at 50% 30%,#4a4a4c,var(--dark) 55%,#232325)}
.brand{display:flex;align-items:center;gap:10px}
.brand-name{font-family:"Titillium Web",sans-serif;font-size:19px;font-weight:600;color:var(--orange);line-height:22px;text-transform:uppercase;letter-spacing:.5px}
.brand-mark{width:18px;height:18px;background:var(--orange)}
.nav{top:48px;left:382px;display:flex;gap:30px;font-family:"Titillium Web",sans-serif;font-size:14px;color:#fff;text-transform:uppercase}
.nav .active{color:var(--orange);border-bottom:2px solid var(--orange);padding-bottom:8px}
.circle-arrow{position:absolute;width:54px;height:54px;border-radius:50%;border:1.5px solid #fff}
.circle-arrow svg{position:absolute;left:17px;top:16px}
.circle-arrow.orange{border-color:var(--orange)}

/* services */
.service-card{position:absolute;width:460px;height:130px;background:#fff;box-shadow:0 4px 14px rgba(0,0,0,.08)}
.service-card svg{position:absolute;left:32px;top:38px}
.service-card h3{position:absolute;left:120px;top:22px;font-family:"Titillium Web",sans-serif;font-weight:600;font-size:18px;letter-spacing:1px;color:var(--ink);text-transform:uppercase}
.service-card p{position:absolute;left:120px;top:62px;width:300px;font-size:13px;line-height:22px;color:#666}

/* team */
.photo{position:absolute;width:283px;height:340px}
.expert{position:absolute;width:283px}
.expert h4{font-family:"Titillium Web",sans-serif;font-size:24px;font-weight:600;color:var(--orange);letter-spacing:1px;text-transform:uppercase}
.expert .role{font-size:17px;color:#555;margin-top:4px}
.expert p{font-size:13px;line-height:23px;color:#666;margin-top:6px}

/* testimonials */
.quote-card{position:absolute;top:3133px;width:300px;height:237px;background:#fff;border-radius:8px;box-shadow:0 4px 14px rgba(0,0,0,.1);padding:22px 22px}
.quote-card p{font-size:12.5px;line-height:21.5px;color:#555}
.quote-card .who{position:absolute;right:10px;bottom:20px;text-align:left}
.quote-card .who strong{display:block;font-family:"Titillium Web",sans-serif;font-weight:600;font-size:17px;color:var(--orange);text-transform:uppercase}
.quote-card .who em{font-size:12px;color:#555;padding-left:18px}
.quote-card .qmark{position:absolute;right:150px;bottom:22px;font-family:"Titillium Web",sans-serif;font-size:64px;line-height:40px;color:#f8c6a5;font-weight:700}
.avatar{position:absolute;top:3347px;width:78px;height:78px;border-radius:50%;border:3px solid #fff;background:linear-gradient(160deg,#b7a497,#5a5350);box-shadow:0 2px 8px rgba(0,0,0,.2)}

/* contact */
.field{position:absolute;height:38px;border:1px solid #f5b088;border-radius:6px;font-size:12px;color:#999;padding:10px 10px}

/* footer */
.footer-col h5{font-family:"Titillium Web",sans-serif;font-weight:700;font-size:18px;color:var(--orange);text-transform:uppercase;margin-bottom:24px}
.footer-col li{list-style:none;font-size:13px;color:#bbb;line-height:29px}
.social{width:26px;height:26px;border-radius:50%;border:1.5px solid var(--orange);display:inline-block;margin-right:8px}
</style>
</head>
<body>

<!-- HERO -->
<header class="abs hero">
  <div class="hero-backdrop" role="img" aria-label="Dark textured background with a subtle connected-network motif"></div>
  <svg class="abs" style="left:0;top:0" width="1200" height="625" aria-hidden="true">
    <path d="M0 560 Q600 660 1200 560 L1200 625 L0 625 Z" fill="#fff"/>
  </svg>
  <div class="abs brand" style="left:110px;top:20px">
    <div class="brand-name">Halvern Ridge<br>Advisory LLC</div>
    <div class="brand-mark"></div>
  </div>
  <nav class="abs nav">
    <span class="active">Home</span><span>About Us</span><span>Our Experts</span><span>News and Events</span><span>Careers</span>
  </nav>
  <svg class="abs" style="left:906px;top:48px" width="30" height="20" aria-hidden="true"><line x1="0.5" y1="0" x2="0.5" y2="20" stroke="#f26a1b"/><circle cx="18" cy="8" r="6" stroke="#f26a1b" stroke-width="2" fill="none"/><line x1="22.5" y1="12.5" x2="28" y2="18" stroke="#f26a1b" stroke-width="2"/></svg>
  <div class="abs btn btn-fill" style="left:950px;top:36px;width:138px;height:42px">Contact Us</div>

  <h1 class="abs center heading-font" style="top:222px;font-size:46px;font-weight:700;color:#fff;letter-spacing:1px;text-transform:uppercase">Halvern Ridge Advisory LLC</h1>
  <p class="abs center" style="top:292px;font-size:16px;line-height:27px;color:#fff">Sed ut perspiciatis unde omnis iste natus error sit volup<br>tatem accusa ntium.</p>
  <div class="abs btn btn-fill" style="left:403px;top:361px;width:186px">Get Started</div>
  <div class="abs btn btn-line" style="left:609px;top:361px;width:184px">Free Consultation</div>
  <div class="circle-arrow" style="left:27px;top:303px"><svg width="20" height="22"><path d="M13 2 L4 11 L13 20" stroke="#fff" stroke-width="2" fill="none"/></svg></div>
  <div class="circle-arrow" style="left:1114px;top:303px"><svg width="20" height="22"><path d="M7 2 L16 11 L7 20" stroke="#fff" stroke-width="2" fill="none"/></svg></div>
</header>

<!-- scroll cue -->
<svg class="abs" style="left:588px;top:617px" width="24" height="40" aria-hidden="true"><rect x="2" y="2" width="20" height="34" rx="10" fill="#fff" stroke="#f26a1b" stroke-width="2"/><line x1="12" y1="9" x2="12" y2="16" stroke="#f26a1b" stroke-width="2"/></svg>
<div class="vline" style="top:657px;height:68px"></div>

<!-- ABOUT -->
<section>
  <div class="abs center eyebrow" style="top:765px">About Halvern</div>
  <h2 class="abs center section-title" style="top:797px">Who We Are</h2>
  <p class="abs center copy" style="top:864px">Sed ut perspiciatis unde omnis iste natus error sit voluptatem accusantium doloremqu</p>
  <p class="abs copy" style="left:150px;width:900px;text-align:center;top:904px">Tillo inventore veritatis et quasi architecto beatae vitae dicta sunt explicabo. Nemo enim ipsam voluptatem quia voluptas sit aspernatur aut odit aut fugit, sed quia consequuntur magni dolores eos qui ratione voluptatem sequi nesciunt.</p>
  <p class="abs copy" style="left:190px;width:820px;text-align:center;top:974px">Folor sit amet, consectetur, adipisci velit, sed quia non numquam eius modi tempora incidunt ut labore et dolore magnam aliquam quaerat voluptatem. Ut enim ad minima veniam, quis nostrum exercitationem ullam corporis suscipit laboriosam, nisi ut aliquid ex ea commodi consequatur</p>
  <div class="abs btn btn-fill" style="left:507px;top:1078px;width:186px">Read More</div>
</section>
<div class="vline" style="top:1165px;height:95px;z-index:2"></div>

<!-- SERVICES -->
<section>
  <svg class="abs" style="left:0;top:1215px" width="1200" height="880" aria-hidden="true">
    <path d="M0 0 Q600 75 1200 0 L1200 880 Q600 790 0 880 Z" fill="var(--peach)"/>
  </svg>
  <div class="abs center eyebrow" style="top:1324px">Services</div>
  <h2 class="abs center section-title" style="top:1356px">What We Do</h2>
  <p class="abs copy" style="left:270px;width:660px;text-align:center;top:1410px">Sed ut perspiciatis unde omnis iste natus error sit voluptatem accusantium doloremque laudantium, totam rem aperia meaque ipsa quae.</p>

  <div class="service-card" style="left:124px;top:1502px">
    <svg width="54" height="54" aria-hidden="true" fill="none" stroke="#f26a1b" stroke-width="2"><rect x="4" y="8" width="46" height="30" rx="2"/><line x1="16" y1="48" x2="38" y2="48"/><line x1="27" y1="38" x2="27" y2="48"/><circle cx="27" cy="23" r="7"/></svg>
    <h3>IT</h3><p>Sed ut perspiciatis unde omnis iste natus error sit voluptatem accusantium doloremque.</p>
  </div>
  <div class="service-card" style="left:614px;top:1502px">
    <svg width="54" height="54" aria-hidden="true" fill="none" stroke="#f26a1b" stroke-width="2"><circle cx="30" cy="18" r="12"/><circle cx="30" cy="18" r="4"/><path d="M4 44 L16 38 L30 42 L46 34 M16 38 L20 50 L40 46"/></svg>
    <h3>Cyber Security</h3><p>Sed ut perspiciatis unde omnis iste natus error sit voluptatem accusantium doloremque.</p>
  </div>
  <div class="service-card" style="left:124px;top:1655px">
    <svg width="54" height="54" aria-hidden="true" fill="none" stroke="#f26a1b" stroke-width="2"><circle cx="27" cy="27" r="22"/><circle cx="27" cy="27" r="13"/><circle cx="27" cy="27" r="5"/></svg>
    <h3>Risk</h3><p>Sed ut perspiciatis unde omnis iste natus error sit voluptatem accusantium doloremque.</p>
  </div>
  <div class="service-card" style="left:614px;top:1655px">
    <svg width="54" height="54" aria-hidden="true" fill="none" stroke="#f26a1b" stroke-width="2"><circle cx="27" cy="12" r="6"/><path d="M15 34 Q27 18 39 34 M6 22 L14 40 L40 40 L48 22"/><line x1="27" y1="40" x2="27" y2="50"/></svg>
    <h3>Project Management</h3><p>Sed ut perspiciatis unde omnis iste natus error sit voluptatem accusantium doloremque.</p>
  </div>
  <div class="service-card" style="left:262px;top:1805px;width:674px">
    <svg width="54" height="54" aria-hidden="true" fill="none" stroke="#f26a1b" stroke-width="2"><circle cx="22" cy="22" r="16"/><line x1="34" y1="34" x2="50" y2="50" stroke-width="3"/><path d="M12 26 L19 19 L24 24 L32 16"/></svg>
    <h3>Data Analytics Consulting Services Worldwide</h3><p>Sed ut perspiciatis unde omnis iste natus error sit voluptatem accusantium doloremque.</p>
  </div>
</section>
<div class="vline" style="top:2045px;height:80px"></div>

<!-- TEAM -->
<section>
  <div class="abs center eyebrow" style="top:2148px">Team</div>
  <h2 class="abs center section-title" style="top:2180px">Our Experts</h2>
  <div class="photo" role="img" aria-label="Portrait photo of a consultant in a dark suit" style="left:111px;top:2290px;background:linear-gradient(180deg,#e6e4e1,#b9b4ae 60%,#3a3a3c)"></div>
  <div class="photo" role="img" aria-label="Portrait photo of a consultant in a blue jacket" style="left:458px;top:2290px;background:linear-gradient(180deg,#eef0f2,#c6ccd2 60%,#2f4a6e)"></div>
  <div class="photo" role="img" aria-label="Portrait photo of a consultant in a navy blazer" style="left:805px;top:2290px;background:linear-gradient(180deg,#dfe3e8,#b8bec6 60%,#2a3246)"></div>
  <div class="expert" style="left:113px;top:2642px"><h4>Marcus Ellery</h4><div class="role">CEO</div><p>Sed ut perspiciatis unde omnis iste natus voluptatem accusantium doloremque.</p></div>
  <div class="expert" style="left:460px;top:2642px"><h4>Marcus Ellery</h4><div class="role">CEO</div><p>Sed ut perspiciatis unde omnis iste natus voluptatem accusantium doloremque.</p></div>
  <div class="expert" style="left:807px;top:2642px"><h4>Marcus Ellery</h4><div class="role">CEO</div><p>Sed ut perspiciatis unde omnis iste natus voluptatem accusantium doloremque.</p></div>
  <div class="circle-arrow orange" style="left:27px;top:2461px"><svg width="20" height="22"><path d="M13 2 L4 11 L13 20" stroke="#f26a1b" stroke-width="2" fill="none"/></svg></div>
  <div class="circle-arrow orange" style="left:1114px;top:2461px"><svg width="20" height="22"><path d="M7 2 L16 11 L7 20" stroke="#f26a1b" stroke-width="2" fill="none"/></svg></div>
</section>

<!-- TESTIMONIALS -->
<section>
  <div class="abs" role="img" aria-label="Group photo of smiling business team members" style="left:0;top:2888px;width:1200px;height:353px;background:linear-gradient(180deg,#6f7176,#8b8c8f 45%,#55585e)"></div>
  <div class="abs center heading-font" style="top:2996px;font-size:19px;color:#fff;letter-spacing:1px">TESTIMONIALS</div>
  <h2 class="abs center section-title" style="top:3028px;color:#fff">What Our Clints Says</h2>

  <div class="quote-card" style="left:111px"><p>"Sed ut perspiciatis unde omnis iste natus error sit voluptatem accusantium dolore mque laudantium, totam rem aperiam, eaque ipsa quae ab illo inventore veritatis et quasi architecto beatae vitae em quia volu ptas sit aspernatur aut odit aut."</p><span class="qmark">“</span><div class="who"><strong>Owen Brandt</strong><em>Delmar, CEO</em></div></div>
  <div class="quote-card" style="left:450px"><p>"Sed ut perspiciatis unde omnis iste natus error sit voluptatem accusantium dolore mque laudantium, xpli cabo. Nemo enim ipsam voluptatem quia volu ptas sit aspernatur aut odit aut."</p><span class="qmark">“</span><div class="who"><strong>Owen Brandt</strong><em>Delmar, CEO</em></div></div>
  <div class="quote-card" style="left:788px"><p>"Sed ut perspiciatis unde omnis iste natus error sit voluptatem accusantium dolore mque laudantium, totam rem aperiam, eaque ipsa quae ab illo inventore veritatis et quasi architecto beatae vitae dicta sunt expli cabo. Nemo enim ipsam vom quia volu ptas sit aspernatur aut odit aut."</p><span class="qmark">“</span><div class="who"><strong>Owen Brandt</strong><em>Delmar, CEO</em></div></div>
  <div class="avatar" role="img" aria-label="Client portrait" style="left:117px"></div>
  <div class="avatar" role="img" aria-label="Client portrait" style="left:456px"></div>
  <div class="avatar" role="img" aria-label="Client portrait" style="left:794px"></div>
  <svg class="abs" style="left:566px;top:3460px" width="70" height="14" aria-hidden="true"><circle cx="7" cy="7" r="5" fill="#f26a1b"/><circle cx="27" cy="7" r="3.5" fill="none" stroke="#888"/><circle cx="43" cy="7" r="3.5" fill="none" stroke="#888"/><circle cx="59" cy="7" r="3.5" fill="none" stroke="#888"/></svg>
</section>

<!-- CONTACT -->
<section>
  <div class="abs" role="img" aria-label="Street map of the office neighbourhood" style="left:0;top:3580px;width:1200px;height:500px;background:linear-gradient(180deg,#eeeeee,#e4e4e4)"></div>
  <svg class="abs" style="left:830px;top:3802px" width="26" height="36" aria-hidden="true"><path d="M13 35 C4 22 1 17 1 12 A12 12 0 0 1 25 12 C25 17 22 22 13 35 Z" fill="#f26a1b"/><circle cx="13" cy="12" r="4.5" fill="#fff"/></svg>
  <div class="abs" style="left:111px;top:3692px;width:461px;height:443px;background:#fff;box-shadow:0 4px 16px rgba(0,0,0,.12);z-index:3">
    <h2 class="section-title" style="position:absolute;left:0;width:461px;text-align:center;top:18px">Contact Us</h2>
    <p style="position:absolute;left:40px;width:381px;text-align:center;top:72px;font-size:12.5px;line-height:22px;color:#666">"Sed ut perspiciatis unde omnis iste natus error sit voluptatem accusantium dolore mque.</p>
    <div class="field" style="left:37px;top:121px;width:180px">First Name</div>
    <div class="field" style="left:235px;top:121px;width:180px">Last Name</div>
    <div class="field" style="left:37px;top:173px;width:180px">Email</div>
    <div class="field" style="left:235px;top:173px;width:180px">Phone</div>
    <div class="field" style="left:37px;top:225px;width:378px;height:130px">Message</div>
    <div class="btn btn-fill" style="position:absolute;left:37px;top:373px;width:186px">Submit</div>
  </div>
</section>

<!-- FOOTER -->
<footer>
  <svg class="abs" style="left:0;top:4035px" width="1200" height="535" aria-hidden="true"><path d="M0 40 Q600 -20 1200 40 L1200 535 L0 535 Z" fill="#1a1a1a"/></svg>
  <div class="abs brand" style="left:111px;top:4202px">
    <div class="brand-name">Halvern Ridge<br>Advisory LLC</div>
    <div class="brand-mark"></div>
  </div>
  <p class="abs" style="left:111px;top:4290px;width:270px;font-size:13px;line-height:24px;color:#aaa">Aequasi architecto beatae vitae dicta sunt explicabo. Nemo enim ipsam voluptatem quia voluptas sit aspernatur aut odit aut fugit, sed quia consendoler sit amet.</p>
  <div class="abs" style="left:111px;top:4414px"><span class="social"></span><span class="social"></span><span class="social"></span></div>

  <div class="abs footer-col" style="left:421px;top:4208px"><h5>Quick Links</h5><ul><li>Home</li><li>About Us</li><li>Our Experts</li><li>News and Events</li><li>Careers</li></ul></div>
  <div class="abs footer-col" style="left:593px;top:4208px;width:220px"><h5>Address</h5>
    <ul>
      <li><svg width="14" height="14" style="vertical-align:-2px;margin-right:10px"><path d="M3 1 L6 1 L7 4 L5 6 Q7 9 9 9 L11 7 L13 8 L13 12 Q6 13 2 5 Z" fill="#f26a1b"/></svg>555 018 2240</li>
      <li><svg width="14" height="12" style="vertical-align:-1px;margin-right:10px"><rect x="1" y="1" width="12" height="10" fill="none" stroke="#f26a1b" stroke-width="1.5"/><path d="M1 1 L7 7 L13 1" fill="none" stroke="#f26a1b" stroke-width="1.5"/></svg>halvern.advisory@mail.example</li>
      <li style="display:flex;align-items:flex-start;line-height:26px"><svg width="14" height="18" style="margin:4px 10px 0 0;flex:none"><path d="M7 17 C2 10 1 8 1 6 A6 6 0 0 1 13 6 C13 8 12 10 7 17 Z" fill="#f26a1b"/><circle cx="7" cy="6" r="2" fill="#1a1a1a"/></svg><span>4120 Larkfield Road,<br>Denholm,<br>North Carolina, 27410,<br>USA</span></li>
    </ul>
  </div>
  <div class="abs footer-col" style="left:837px;top:4208px"><h5>Contact</h5><ul><li>Contact</li><li>Private details</li><li>Privacy Policy</li><li>Terms &amp; conditions</li><li>Site Map</li></ul></div>
  <div class="abs footer-col" style="left:1005px;top:4208px"><h5>Support</h5><ul><li>Home</li><li>Industries</li><li>support</li></ul></div>

  <div class="abs" style="left:111px;top:4505px;width:978px;height:1px;background:#3a3a3a"></div>
  <p class="abs center" style="top:4520px;font-size:13px;color:#aaa">Copyrights © 2020 All Rights Reserved</p>
</footer>

</body>
</html>
```